" Somos um empresa que deseja promover o bem estar, conhecimento do corpo e sexo como algo natural e importante para vida de todos. Nossos produtos sao hi-tech sex toys e apps "

```html
<!DOCTYPE html>
<html lang="pt-BR">
<head>
<meta charset="UTF-8">
<title>Velunara – Cartões de visita</title>
<link rel="stylesheet" href="https://fonts.googleapis.com/css2?family=Cinzel:wght@400;500&display=swap">
<style>
  :root {
    --page: #e6e2dc;
    --card: #1c1a1a;
    --gold: #c9a45c;
    --gold-soft: #a88a52;
    --rule: #4a4238;
  }
  * { margin: 0; padding: 0; box-sizing: border-box; }
  html, body {
    width: 1200px;
    height: 1200px;
    overflow: hidden;
    background: var(--page);
  }
  .canvas {
    position: relative;
    width: 1200px;
    height: 1200px;
    display: flex;
    align-items: center;
    justify-content: center;
    gap: 60px;
    font-family: "Cinzel", serif;
  }
  .card {
    width: 520px;
    height: 300px;
    background: var(--card);
    color: var(--gold);
    position: relative;
  }
  .card--front {
    display: flex;
    flex-direction: column;
    align-items: center;
    justify-content: center;
  }
  .brand-name {
    font-weight: 500;
    font-size: 52px;
    letter-spacing: 3px;
    color: var(--gold);
    line-height: 1;
  }
  .brand-tagline {
    margin-top: 10px;
    font-weight: 500;
    font-size: 9px;
    letter-spacing: 5px;
    color: var(--gold-soft);
  }
  .card--back { padding: 0 28px; }
  .back-header {
    height: 96px;
    display: flex;
    flex-direction: column;
    align-items: center;
    justify-content: center;
    border-bottom: 1px solid var(--rule);
  }
  .back-header .brand-name { font-size: 32px; letter-spacing: 2px; }
  .back-header .brand-tagline { font-size: 7px; margin-top: 6px; letter-spacing: 4px; }
  .back-body {
    display: flex;
    padding-top: 40px;
  }
  .person { width: 238px; padding-right: 18px; }
  .person-name {
    font-size: 17px;
    font-weight: 500;
    letter-spacing: 1px;
    color: var(--gold);
  }
  .person-role {
    font-size: 8px;
    letter-spacing: 1px;
    color: var(--gold-soft);
    margin-top: 4px;
  }
  .contact-list {
    list-style: none;
    margin-top: 22px;
    font-size: 8px;
    line-height: 1.7;
    letter-spacing: 0.8px;
    color: var(--gold-soft);
  }
  .divider {
    width: 1px;
    height: 110px;
    background: var(--rule);
    margin-top: 10px;
  }
  .address {
    font-style: normal;
    padding-left: 16px;
    padding-top: 56px;
    font-size: 8px;
    line-height: 1.7;
    letter-spacing: 0.8px;
    color: var(--gold-soft);
  }
</style>
</head>
<body>
  <main class="canvas">
    <section class="card card--front" aria-label="Frente do cartão">
      <div class="brand-name">VELUNARA</div>
      <div class="brand-tagline">MINDFUL WELLBEING</div>
    </section>

    <section class="card card--back" aria-label="Verso do cartão">
      <header class="back-header">
        <div class="brand-name">VELUNARA</div>
        <div class="brand-tagline">MINDFUL WELLBEING</div>
      </header>
      <div class="back-body">
        <div class="person">
          <div class="person-name">NOME SOBRENOME</div>
          <div class="person-role">CARGO</div>
          <ul class="contact-list">
            <li>TEL/FAX: 4000-1234</li>
            <li>CONTATO@VELUNARA.COM.BR</li>
            <li>WWW.VELUNARA.COM.BR</li>
          </ul>
        </div>
        <div class="divider"></div>
        <address class="address">
          AV. DAS PALMEIRAS, 88<br>
          JARDIM AZUL - VILA SERENA - SC<br>
          CEP 00000-000
        </address>
      </div>
    </section>
  </main>
</body>
</html>
```